Design a Website Mockup for GhoulTide a Zombie Horror News Website

I need a website design for a Zombie Horror genre website.
It''s just a single page design for a news / blog like presence.
I'd like it to look modern yet gory. Dark colored themed (black with hints of red). I'd like it to have a main header, a news / main content area, separate side bars to feature: latest gallery photo, latest short film, latest movie review, featured artist, and advertising space. A nice footer with room to provide links and copyright info.

That's just the stuff I want it to have, creative output is all you!

Check some of these out for inspiration or an idea of what I'm looking for:
http://www.frightlanternpost.example
http://www.gloomharborfeed.example
http://crimson-vexation.example
http://ashcorpse.example

The audience will be horror fans of all types and ages.

This is the first of 4 websites I want designed. Whoever I end up choosing (or possibly even the top 3 designers) will also have a chance at being hired to do the design for the other 3 websites.

```html
<!DOCTYPE html>
<html lang="en">
<head>
<meta charset="utf-8">
<title>GhoulTide — Zombie Horror News</title>
<link href="https://fonts.googleapis.com/css2?family=Jolly+Lodger&family=Creepster&family=Tinos:wght@400&family=Arimo:wght@400;700&display=swap" rel="stylesheet">
<style>
:root{
  --bg:#000;
  --blood:#c4141a;
  --blood-bright:#e01e22;
  --blood-deep:#6e0a0d;
  --blood-dark:#3a0507;
  --text:#b9b9b9;
  --muted:#7d7d7d;
  --frame:#8a8a8a;
  --gold:#c6a23a;
}
*{margin:0;padding:0;box-sizing:border-box}
html,body{width:1200px;height:2849px;overflow:hidden;background:var(--bg)}
body{position:relative;font-family:"Tinos",serif;color:var(--text)}
.abs{position:absolute}
.grain{position:absolute;left:0;top:0;width:100%;height:100%;pointer-events:none}

/* header */
.site-header{left:0;top:0;width:1200px;height:520px;
  background:
    radial-gradient(ellipse 220px 90px at 290px 150px,rgba(150,10,14,.55),transparent 70%),
    radial-gradient(ellipse 300px 200px at 1130px 120px,rgba(0,0,0,.75),transparent 70%),
    radial-gradient(ellipse 260px 260px at 40px 260px,rgba(0,0,0,.9),transparent 70%),
    linear-gradient(#4a4a4a 0,#2e2e2e 110px,#161616 240px,#000 400px)}
.brand{left:168px;top:48px;width:260px;height:100px;display:flex;align-items:center;gap:12px}
.brand-mark{width:22px;height:22px;background:var(--blood);border-radius:50%}
.brand-name{font-family:"Tinos",serif;font-size:40px;color:#d8d8d8;letter-spacing:1px}
.nav-panel{left:456px;top:11px;width:590px;height:128px;border:3px solid #4c4c4c;border-radius:6px;overflow:hidden;
  background:
    radial-gradient(ellipse 120px 60px at 380px 70px,rgba(150,12,16,.45),transparent 70%),
    radial-gradient(ellipse 90px 50px at 110px 20px,rgba(170,12,16,.55),transparent 70%),
    linear-gradient(#3d3232,#1a1313)}
.nav-news-box{left:2px;top:70px;width:130px;height:54px;border:2px solid #555;background:#160d0b}
.nav-news{left:14px;top:6px;font-family:"Creepster",cursive;font-size:38px;letter-spacing:2px;
  color:#ff6a18;text-shadow:0 0 6px #ff2a00,0 0 2px #ffb000}
.nav-link{font-family:"Arimo",sans-serif;font-weight:700;font-size:17px;color:var(--blood-bright)}
.hazard{right:6px;bottom:6px;width:22px;height:46px;
  background:repeating-linear-gradient(135deg,#d8b800 0 6px,#111 6px 12px)}
.social{width:26px;height:22px;background:#4f5f88;border-radius:3px}

.slider{left:171px;top:191px;width:858px;height:292px;border:2px solid #5a0a0a;overflow:hidden;
  box-shadow:0 0 10px rgba(150,0,0,.5);
  background:
    radial-gradient(ellipse 520px 90px at 50% 78%,rgba(20,24,22,.9),transparent 70%),
    radial-gradient(ellipse 220px 140px at 60% 35%,rgba(150,160,150,.35),transparent 70%),
    linear-gradient(#5e6864 0,#3d4844 35%,#262e2b 65%,#111514)}
.slider-caption{left:0;width:100%;bottom:12px;text-align:center;font-family:"Arimo",sans-serif;font-weight:700;font-size:13px;color:#fff}
.slider-caption span{color:var(--blood);text-decoration:underline;font-weight:400}
.dots{left:552px;top:494px;display:flex;gap:10px}
.dots i{width:10px;height:10px;border-radius:50%;background:var(--blood-deep)}
.dots i:first-child{background:var(--blood)}

.section-title{font-family:"Jolly Lodger",cursive;color:var(--blood);font-size:50px;line-height:1;font-weight:400}

/* posts */
.post{left:144px;width:571px;height:480px}
.post-band{left:0;top:0;width:550px;height:66px;
  background:
    radial-gradient(ellipse 170px 26px at 430px 56px,rgba(140,12,16,.85),transparent 70%),
    radial-gradient(ellipse 70px 20px at 230px 8px,rgba(140,12,16,.7),transparent 70%),
    linear-gradient(90deg,#0a0a0a 0,#4e4e4e 30%,#3c3030 65%,#000 100%)}
.post-title{left:10px;top:12px;font-family:"Arimo",sans-serif;font-weight:700;font-size:19px;color:var(--blood-bright);
  text-shadow:1px 1px 0 #2a0000}
.post-date{left:10px;top:44px;font-size:12px;color:var(--muted)}
.post-image{left:0;top:84px;width:571px;height:152px}
.post-body{left:0;top:242px;width:571px;font-size:17px;line-height:21px}
.more{width:82px;height:24px;border-radius:12px 4px 12px 4px;
  background:radial-gradient(ellipse 50% 46% at 50% 50%,var(--blood-bright) 40%,var(--blood-deep) 80%,transparent 100%);
  font-family:"Arimo",sans-serif;font-weight:700;font-size:15px;color:#eee;text-align:center;line-height:24px;text-shadow:1px 1px 0 #000}
.post .more{left:484px;top:434px}

/* sidebar */
.side-frame{left:771px;width:286px;height:256px;border:2px solid var(--frame);padding:8px}
.side-fill{width:100%;height:100%}
.side-text{left:771px;width:290px;font-size:17px;line-height:21px}
.side-date{left:771px;font-size:9px;color:var(--muted)}
.side-more{left:776px}

/* footer */
.site-footer{left:0;top:2637px;width:1200px;height:212px;border-top:3px solid #242424;
  background:
    radial-gradient(ellipse 140px 80px at 830px 110px,rgba(120,10,14,.35),transparent 70%),
    linear-gradient(#1a1a1a,#0a0a0a)}
.foot-link{font-family:"Jolly Lodger",cursive;font-size:32px;color:var(--gold)}
.copyright{left:0;width:1200px;top:186px;text-align:center;font-family:"Arimo",sans-serif;font-size:11px;color:#5e5e5e}
</style>
</head>
<body>

<svg width="0" height="0" style="position:absolute">
  <filter id="grunge"><feTurbulence type="fractalNoise" baseFrequency=".9" numOctaves="3" seed="4"/><feColorMatrix values="0 0 0 0 0  0 0 0 0 0  0 0 0 0 0  0 0 0 .55 0"/></filter>
  <filter id="stain"><feTurbulence type="fractalNoise" baseFrequency=".02" numOctaves="4" seed="9"/><feColorMatrix values="0 0 0 0 .45  0 0 0 0 .02  0 0 0 0 .03  0 0 0 1.4 -.75"/></filter>
</svg>

<header class="site-header abs">
  <svg class="grain" viewBox="0 0 1200 520" preserveAspectRatio="none"><rect width="1200" height="360" filter="url(#grunge)"/><rect width="1200" height="200" filter="url(#stain)" opacity=".6"/></svg>
  <div class="brand abs"><span class="brand-mark"></span><span class="brand-name">GhoulTide</span></div>

  <span class="social abs" style="left:524px;top:20px"></span>
  <span class="social abs" style="left:524px;top:47px"></span>

  <nav class="nav-panel abs">
    <div class="nav-news-box abs"><span class="nav-news abs">NEWS</span></div>
    <span class="nav-link abs" style="left:153px;top:18px">Latest Movie Review</span>
    <span class="nav-link abs" style="left:380px;top:18px">Latest Short Film</span>
    <span class="nav-link abs" style="left:162px;top:80px">Featured Artist</span>
    <span class="nav-link abs" style="left:380px;top:80px">Latest Gallery Photo</span>
    <span class="hazard abs"></span>
  </nav>

  <div class="slider abs" role="img" aria-label="Ruined city street filled with a zombie horde">
    <svg class="grain" viewBox="0 0 858 292" preserveAspectRatio="none"><rect width="858" height="292" filter="url(#grunge)" opacity=".8"/></svg>
    <p class="slider-caption abs">Welcome to <span>GhoulTide</span>. Enjoy the latest news about zombies!</p>
  </div>
  <div class="dots abs"><i></i><i></i><i></i><i></i><i></i></div>
</header>

<h2 class="section-title abs" style="left:153px;top:522px">News</h2>

<article class="post abs" style="top:583px">
  <div class="post-band abs"></div>
  <h3 class="post-title abs">First testing new</h3>
  <p class="post-date abs">Date: June 07, 2014</p>
  <div class="post-image abs" role="img" aria-label="Lone figure on a misty pier" style="background:radial-gradient(ellipse 260px 90px at 50% 20%,#8a9698,transparent 70%),linear-gradient(#5a6668,#38403f 55%,#1c2020)"></div>
  <p class="post-body abs">Nunc varius venenatis sem sed adipiscing. Mauris suscipit mauris in purus mattis placerat. Ut rhoncus imperdiet nibh sit amet sagittis. Aliquam erat volutpat. In pellentesque sagittis dictum. Aliquam erat volutpat. Donec ac aliquam neque. Donec quis tortor nec erat fringilla vulputate. Aliquam erat volutpat. In pellentesque sagittis dictum. Aliquam erat volutpat. Donec ac aliquam neque. Sed tellus diam, consequat nec volutpat et, cursus ac nisi. Mauris in risus in diam consequat suscipit non ac enim. Etiam massa augue, porttitor quis laoreet sit amet, porttitor sed tortor.</p>
  <span class="more abs">More</span>
</article>

<article class="post abs" style="top:1091px">
  <div class="post-band abs"></div>
  <h3 class="post-title abs">Another testing new</h3>
  <p class="post-date abs">Date: June 06, 2014</p>
  <div class="post-image abs" role="img" aria-label="Monster creature in a bright street" style="background:radial-gradient(ellipse 90px 70px at 44% 50%,#5a2c2a,transparent 75%),linear-gradient(90deg,#2a2a2a,#4a3c3a 35%,#8a7a78 60%,#ececf0)"></div>
  <p class="post-body abs">Nunc varius venenatis sem sed adipiscing. Mauris suscipit mauris in purus mattis placerat. Ut rhoncus imperdiet nibh sit amet sagittis. Aliquam erat volutpat. In pellentesque sagittis dictum. Aliquam erat volutpat. Donec ac aliquam neque. Donec quis tortor nec erat fringilla vulputate. Aliquam erat volutpat. In pellentesque sagittis dictum. Aliquam erat volutpat. Donec ac aliquam neque. Sed tellus diam, consequat nec volutpat et, cursus ac nisi. Mauris in risus in diam consequat suscipit non ac enim. Etiam massa augue, porttitor quis laoreet sit amet, porttitor sed tortor.</p>
  <span class="more abs">More</span>
</article>

<article class="post abs" style="top:1599px">
  <div class="post-band abs"></div>
  <h3 class="post-title abs">Last testing new</h3>
  <p class="post-date abs">Date: June 05, 2014</p>
  <div class="post-image abs" role="img" aria-label="Crowded old graveyard with mossy headstones" style="background:radial-gradient(ellipse 200px 40px at 25% 85%,#2e7a26,transparent 70%),linear-gradient(#3a3a38,#6b6a60 45%,#4a5a3a 75%,#1e3a18)"></div>
  <p class="post-body abs">Nunc varius venenatis sem sed adipiscing. Mauris suscipit mauris in purus mattis placerat. Ut rhoncus imperdiet nibh sit amet sagittis. Aliquam erat volutpat. In pellentesque sagittis dictum. Aliquam erat volutpat. Donec ac aliquam neque. Donec quis tortor nec erat fringilla vulputate. Aliquam erat volutpat. In pellentesque sagittis dictum. Aliquam erat volutpat. Donec ac aliquam neque. Sed tellus diam, consequat nec volutpat et, cursus ac nisi. Mauris in risus in diam consequat suscipit non ac enim. Etiam massa augue, porttitor quis laoreet sit amet, porttitor sed tortor.</p>
  <span class="more abs">More</span>
</article>

<article class="post abs" style="top:2107px">
  <div class="post-band abs"></div>
  <h3 class="post-title abs">Last testing new</h3>
  <p class="post-date abs">Date: June 01, 2014</p>
  <div class="post-image abs" role="img" aria-label="Horde of zombies crowding forward" style="background:radial-gradient(ellipse 180px 70px at 45% 50%,#7a5e3e,transparent 75%),linear-gradient(#2a2018,#5a4430 50%,#1e160e)"></div>
  <p class="post-body abs">Nunc varius venenatis sem sed adipiscing. Mauris suscipit mauris in purus mattis placerat. Ut rhoncus imperdiet nibh sit amet sagittis. Aliquam erat volutpat. In pellentesque sagittis dictum. Aliquam erat volutpat. Donec ac aliquam neque. Donec quis tortor nec erat fringilla vulputate. Aliquam erat volutpat. In pellentesque sagittis dictum. Aliquam erat volutpat. Donec ac aliquam neque. Sed tellus diam, consequat nec volutpat et, cursus ac nisi. Mauris in risus in diam consequat suscipit non ac enim. Etiam massa augue, porttitor quis laoreet sit amet, porttitor sed tortor.</p>
  <span class="more abs">More</span>
</article>

<aside>
  <h2 class="section-title abs" style="left:771px;top:524px">Advertisement</h2>
  <div class="side-frame abs" style="top:595px">
    <div class="side-fill" style="background:#fff;display:flex;align-items:center;justify-content:center;gap:10px">
      <span style="width:18px;height:18px;border-radius:50%;background:#1e6b3c"></span>
      <span style="font-family:'Tinos',serif;font-size:30px;color:#1e6b3c">Bloodbrew</span>
    </div>
  </div>

  <h2 class="section-title abs" style="left:771px;top:898px">Movie Review</h2>
  <p class="abs" style="left:771px;top:962px;font-family:'Arimo',sans-serif;font-weight:700;font-size:16px;color:var(--blood-bright)">Rot Planet rules!</p>
  <p class="side-text abs" style="top:997px">Morbi pellentesque, libero vitae fermentum tincidunt libero accumsan erat, sit amet ornare.</p>
  <p class="side-date abs" style="top:1066px">May 14, 2014</p>
  <span class="more side-more abs" style="top:1101px">More</span>

  <h2 class="section-title abs" style="left:771px;top:1158px">Short film</h2>
  <div class="side-frame abs" style="top:1227px">
    <div class="side-fill" role="img" aria-label="Close-up of a zombie" style="background:radial-gradient(ellipse 90px 110px at 45% 45%,#9a8a5a,transparent 75%),linear-gradient(135deg,#7a6c40,#4a4a2c 60%,#262a1e)"></div>
  </div>
  <p class="side-text abs" style="top:1482px">Duis convallis odio et velit venenatis ac venenatis turpis mattis varius quam et laoreet.</p>
  <p class="side-date abs" style="top:1551px">May 14, 2014</p>
  <span class="more side-more abs" style="top:1587px">More</span>

  <h2 class="section-title abs" style="left:775px;top:1639px">Latest gallery photo</h2>
  <div class="side-frame abs" style="top:1721px">
    <div class="side-fill" role="img" aria-label="Snarling bloodied zombie in the dark" style="background:radial-gradient(ellipse 70px 60px at 50% 68%,#8a1a14,transparent 75%),radial-gradient(circle at 50% 50%,#4a2a24,#140e0d 75%)"></div>
  </div>
  <p class="side-text abs" style="top:1977px">Duis convallis odio et velit venenatis ac venenatis turpis mattis varius quam et laoreet.</p>
  <p class="side-date abs" style="top:2046px">May 14, 2014</p>
  <span class="more side-more abs" style="top:2083px">More</span>

  <h2 class="section-title abs" style="left:771px;top:2135px">Featured Artist</h2>
  <div class="side-frame abs" style="top:2203px">
    <div class="side-fill" role="img" aria-label="Artwork of zombies around a glowing blue hatch" style="background:radial-gradient(circle at 50% 55%,#cdeeff,#3a7ab0 16%,#2a2a30 50%,#121212)"></div>
  </div>
  <p class="side-text abs" style="top:2459px">Duis convallis odio et velit venenatis ac venenatis turpis mattis varius quam et laoreet.</p>
  <p class="side-date abs" style="top:2528px">May 14, 2014</p>
  <span class="more side-more abs" style="top:2564px">More</span>
</aside>

<footer class="site-footer abs">
  <svg class="grain" viewBox="0 0 1200 212" preserveAspectRatio="none"><rect width="1200" height="212" filter="url(#grunge)" opacity=".7"/></svg>
  <h2 class="section-title abs" style="left:240px;top:14px;font-size:60px;color:var(--blood-deep)">Useful links</h2>
  <a class="foot-link abs" style="left:227px;top:84px">About Us</a>
  <a class="foot-link abs" style="left:373px;top:84px">Subscribe</a>
  <a class="foot-link abs" style="left:217px;top:126px">Contact Us</a>
  <a class="foot-link abs" style="left:385px;top:126px">Legal</a>
  <div class="abs" role="img" aria-label="Keep out warning tag" style="left:506px;top:30px;width:114px;height:60px;background:linear-gradient(#d6b437,#a8861e);border-radius:6px;transform:rotate(10deg)"></div>
  <div class="abs" style="left:752px;top:56px;display:flex;align-items:center;gap:10px">
    <span style="width:16px;height:16px;background:var(--blood);border-radius:50%"></span>
    <span style="font-family:'Tinos',serif;font-size:30px;color:#d8d8d8">GhoulTide</span>
  </div>
  <p class="copyright abs">© 2014 GhoulTide. All rights reserved.</p>
</footer>

</body>
</html>
```